Stationery Design Project

KT7 Staffing requires letterhead and business card designs for a company based in London. Just like the name, we're a management resourcing company, providing resources to third party companies. You can see www.kt7staffing-example.com for ideas on existing colour schemes and design concepts that have been implimented and agreed to. Ultimately the design should broadcast professionalism, safety and the concept of growth.

Target Market(s)

Financial institutes; friendly societies (All UK based)

Industry/Entity Type

Safety

Requirements
Must have
• Files produced should be print ready; and the text in them editable (eg address, name etc)

```html
<!DOCTYPE html>
<html lang="en">
<head>
<meta charset="utf-8">
<title>KT7 Staffing – Letterhead</title>
<link rel="stylesheet" href="https://fonts.googleapis.com/css2?family=Lato:wght@400;700&display=swap">
<style>
  :root {
    --paper: #ffffff;
    --header-tint: #e9f5fb;
    --brand-teal: #1a8b8c;
    --band-light: #6cb7d8;
    --band-deep: #1e9fae;
    --ink: #2b2b2b;
    --footer-ink: #ffffff;
  }
  html, body {
    margin: 0;
    padding: 0;
    width: 900px;
    height: 1200px;
    overflow: hidden;
    background: var(--paper);
  }
  .letterhead {
    position: relative;
    width: 900px;
    height: 1200px;
    background: var(--paper);
    font-family: "Lato", Arial, sans-serif;
    overflow: hidden;
  }
  .letterhead__waves {
    position: absolute;
    inset: 0;
    width: 900px;
    height: 1200px;
  }
  .header-tint { fill: var(--header-tint); }
  .footer-rule { fill: var(--brand-teal); }
  .footer-band { fill: url(#footerGradient); }

  .brand {
    position: absolute;
    left: 44px;
    top: 52px;
    display: flex;
    align-items: center;
    gap: 14px;
  }
  .brand__dot {
    width: 40px;
    height: 40px;
    border-radius: 50%;
    background: var(--brand-teal);
  }
  .brand__name {
    margin: 0;
    font-size: 38px;
    font-weight: 700;
    color: var(--brand-teal);
    letter-spacing: 0.5px;
    line-height: 1;
  }
  .sender-address {
    position: absolute;
    left: 90px;
    top: 140px;
    margin: 0;
    font-style: normal;
    font-size: 17px;
    line-height: 1.35;
    color: var(--ink);
  }
  .website {
    position: absolute;
    right: 30px;
    bottom: 22px;
    margin: 0;
    font-size: 16px;
    letter-spacing: 3.5px;
    color: var(--footer-ink);
  }
</style>
</head>
<body>
  <main class="letterhead">
    <svg class="letterhead__waves" viewBox="0 0 678 961" preserveAspectRatio="none" aria-hidden="true">
      <defs>
        <linearGradient id="footerGradient" x1="0" y1="0" x2="1" y2="0">
          <stop offset="0" stop-color="#6cb7d8"/>
          <stop offset="1" stop-color="#1e9fae"/>
        </linearGradient>
      </defs>
      <path class="header-tint" d="M0,0 H678 V88 C520,94 370,118 262,170 C190,205 100,212 0,200 Z"/>
      <path class="footer-rule" d="M0,851 C80,900 200,925 320,918 C450,910 560,880 678,876 V961 H0 Z"/>
      <path class="footer-band" d="M0,867 C80,913 200,936 320,930 C450,922 560,892 678,887 V961 H0 Z"/>
    </svg>

    <header class="brand">
      <span class="brand__dot" aria-hidden="true"></span>
      <h1 class="brand__name">KT7 Staffing</h1>
    </header>

    <address class="sender-address">
      48 Harrow Lane, Kingsbury Court<br>
      London, UK NW9 4RT
    </address>

    <footer>
      <p class="website">www.kt7staffing-example.com</p>
    </footer>
  </main>
</body>
</html>
```